Business Card Design Project

I need a cool business card design for the company that will build residential houses.
The card should include:
1) Name: Borek Valdisov
2) Cell: 587.244.XXXX
3) Email: bor.valdisov@qorvina.example
4) Position: General Manager
5) Residential Home Building
6) Company logo that I have uploaded

Industry/Entity Type

Residential

```html
<!DOCTYPE html>
<html lang="en">
<head>
<meta charset="utf-8">
<title>Qorvina Developments – Business Card</title>
<link href="https://fonts.googleapis.com/css2?family=Mulish:wght@400;700&display=swap" rel="stylesheet">
<style>
  :root {
    --backdrop: #4a4a4a;
    --card: #fbfbfb;
    --brand-blue: #1d4f9c;
    --deep-blue: #0f3a8a;
    --brand-green: #5aa52a;
    --ink: #2e2e2e;
    --muted: #6f6f6f;
  }
  html, body {
    margin: 0;
    width: 1200px;
    height: 1000px;
    overflow: hidden;
    background: var(--backdrop);
    font-family: "Mulish", sans-serif;
  }
  .canvas { position: relative; width: 1200px; height: 1000px; }
  .card {
    position: absolute;
    width: 528px;
    height: 302px;
    background: var(--card);
    border-radius: 14px;
    overflow: hidden;
  }
  .card--front { left: 207px; top: 165px; }
  .card--back { left: 472px; top: 534px; }

  .wordmark {
    position: absolute;
    display: flex;
    align-items: center;
    gap: 10px;
    color: var(--brand-blue);
    font-weight: 700;
    line-height: 1.05;
  }
  .wordmark__dot {
    width: 22px; height: 22px;
    border-radius: 50%;
    background: var(--brand-green);
    flex: none;
  }
  .wordmark__name { font-size: 34px; letter-spacing: 1px; }
  .wordmark__name small { display: block; font-size: 13px; letter-spacing: 4.5px; }
  .card--front .wordmark { left: 34px; top: 108px; }
  .card--back .wordmark { left: 72px; top: 112px; }

  .tagline {
    position: absolute;
    right: 303px; top: 204px;
    text-align: right;
    color: var(--muted);
    font-size: 19px;
    line-height: 25px;
  }
  .person { position: absolute; left: 293px; top: 141px; }
  .person__name {
    margin: 0; color: var(--ink);
    font-size: 15px; font-weight: 700; letter-spacing: 0.6px;
  }
  .person__role { margin: 1px 0 0; color: var(--ink); font-size: 12.5px; }
  .contact {
    position: absolute; left: 293px; top: 216px;
    color: var(--ink); font-size: 12.5px; line-height: 16px;
  }
  .contact dt { display: inline; color: var(--deep-blue); font-weight: 700; }
  .contact dd { display: inline; margin: 0; }
  .contact div { margin: 0; }
  .band { position: absolute; bottom: 0; height: 16px; }
  .band--blue { left: 0; width: 261px; background: var(--deep-blue); }
  .band--green { left: 267px; width: 261px; background: var(--brand-green); }
  .wave { position: absolute; left: 0; top: 0; }
</style>
</head>
<body>
<main class="canvas">
  <section class="card card--front" aria-label="Business card front">
    <div class="wordmark">
      <span class="wordmark__dot"></span>
      <span class="wordmark__name">QORVINA<small>DEVELOPMENTS</small></span>
    </div>
    <p class="tagline" style="margin:0">Residential<br>Home Building</p>
    <div class="person">
      <p class="person__name">BOREK VALDISOV</p>
      <p class="person__role">General Manager</p>
    </div>
    <dl class="contact" style="margin:0">
      <div><dt>Cell:</dt> <dd>587.244.XXXX</dd></div>
      <div><dt>Email:</dt> <dd>bor.valdisov@qorvina.example</dd></div>
    </dl>
    <span class="band band--blue"></span>
    <span class="band band--green"></span>
  </section>

  <section class="card card--back" aria-label="Business card back">
    <svg class="wave" width="528" height="302" viewBox="0 0 528 302">
      <path d="M0 228 Q 300 262 528 196 L528 302 L0 302 Z" fill="var(--deep-blue)"/>
      <path d="M0 222 Q 300 256 528 192" fill="none" stroke="#ffffff" stroke-width="5"/>
      <path d="M0 216 Q 300 248 528 188 L528 192 Q 300 254 0 222 Z" fill="var(--brand-green)"/>
    </svg>
    <div class="wordmark">
      <span class="wordmark__dot"></span>
      <span class="wordmark__name">QORVINA<small>DEVELOPMENTS</small></span>
    </div>
  </section>
</main>
</body>
</html>
```